Brightmoor Partners Branding Revamp

We are a consulting company, looking for a way to display and promote our brand. We have 2 sides to the business- Brightmoor (financial) and Partners (cyber security). The financial side products relate to business necessities: card processing, website design/hosting/maintenance, VoIP phone systems. The cyber security side promotes a bundled package of 4 solutions: network vulnerability scan, dark web scan, anti-ransomeware/malware software, and image-level backups. We want people to understand that partnering with Brightmoor Partners gives them “Elevated Peace of Mind” (tagline). Current badge and logos uploaded.

Target Market(s)

Small businesses

Contact Information for Business Card

Lena Marwick, Vice President, lena@brightmoorpartners.example, 555-806-1937, www.brightmoorpartners.example

Requirements
Nice to have
• I do prefer the darker background for front and back

```html
<!DOCTYPE html>
<html lang="en">
<head>
<meta charset="utf-8">
<title>Brightmoor Partners – Business Card</title>
<link href="https://fonts.googleapis.com/css2?family=Titillium+Web:wght@400;600&display=swap" rel="stylesheet">
<style>
  :root {
    --backdrop: #919498;
    --card: #1d1d1f;
    --pattern-deep: #0c0c0d;
    --pattern-mid: #1f2022;
    --pattern-light: #45474c;
    --accent: #e0262b;
    --ink: #f2f2f2;
  }
  * { margin: 0; padding: 0; box-sizing: border-box; }
  html, body {
    width: 1200px; height: 900px; overflow: hidden;
    background: var(--backdrop);
    font-family: "Titillium Web", sans-serif;
  }
  .card {
    position: absolute; left: 363px; width: 475px; height: 271px;
    background: var(--card);
    overflow: hidden;
  }
  .card--front { top: 145px; }
  .card--back { top: 484px; }

  .front-surface {
    position: absolute; inset: 0;
    background:
      linear-gradient(180deg, rgba(255,255,255,0.05) 0%, rgba(0,0,0,0) 40%, rgba(0,0,0,0.35) 100%),
      linear-gradient(100deg, var(--pattern-deep) 0%, var(--pattern-mid) 42%, #2e3033 70%, var(--pattern-light) 100%);
  }
  .front-emblem {
    position: absolute; left: 0; right: 0; top: 114px;
    display: flex; justify-content: center; align-items: center; gap: 12px;
  }
  .front-emblem__dot {
    width: 42px; height: 42px; border-radius: 50%; background: var(--accent);
  }
  .front-emblem__name {
    color: var(--accent); font-weight: 600; font-size: 20px; letter-spacing: 1px;
    text-transform: uppercase;
  }

  .brand {
    position: absolute; left: 0; right: 0; top: 46px;
    display: flex; flex-direction: column; align-items: center; gap: 14px;
  }
  .brand__dot {
    width: 40px; height: 40px; border-radius: 50%; background: var(--accent);
  }
  .brand__name {
    color: var(--ink); font-weight: 600; font-size: 22px; line-height: 24px;
    letter-spacing: 3px; text-transform: uppercase;
  }

  .holder {
    position: absolute; right: 253px; top: 201px; text-align: right;
  }
  .holder__name {
    color: var(--accent); font-weight: 600; font-size: 15px; line-height: 18px;
    text-transform: uppercase;
  }
  .holder__title { color: var(--ink); font-size: 11px; line-height: 16px; }

  .divider {
    position: absolute; left: 237px; top: 196px; width: 1px; height: 40px;
    background: var(--accent);
  }

  .contacts {
    position: absolute; left: 251px; top: 193px; list-style: none;
  }
  .contacts li {
    display: flex; align-items: center; gap: 6px;
    color: var(--ink); font-size: 11px; line-height: 15.3px;
  }
  .contacts svg { width: 9px; height: 9px; flex: none; }
  .contacts .hl { color: var(--accent); }
</style>
</head>
<body>
  <section class="card card--front">
    <div class="front-surface" role="img" aria-label="Embossed repeating triangular brand pattern in dark greys, lighter toward the right"></div>
    <div class="front-emblem">
      <span class="front-emblem__dot"></span>
      <span class="front-emblem__name">Brightmoor Partners</span>
    </div>
  </section>

  <section class="card card--back">
    <div class="brand">
      <span class="brand__dot"></span>
      <span class="brand__name">Brightmoor Partners</span>
    </div>

    <div class="holder">
      <div class="holder__name">Lena Marwick</div>
      <div class="holder__title">Vice President</div>
    </div>

    <span class="divider"></span>

    <ul class="contacts">
      <li>
        <svg viewBox="0 0 10 10" fill="var(--accent)"><path d="M2 0.5 L3.6 2.6 L2.8 3.6 Q4 6 6.4 7.2 L7.4 6.4 L9.5 8 L8.3 9.5 Q1 8 0.5 1.7 Z"/></svg>
        555-806-1937
      </li>
      <li>
        <svg viewBox="0 0 10 10" fill="var(--accent)"><rect x="0.5" y="2" width="9" height="6.4" rx="0.5"/><path d="M0.8 2.4 L5 5.6 L9.2 2.4" stroke="var(--card)" stroke-width="0.9" fill="none"/></svg>
        lena@brightmoorpartners.example
      </li>
      <li>
        <svg viewBox="0 0 10 10" fill="none" stroke="var(--accent)" stroke-width="0.9"><circle cx="5" cy="5" r="4.3"/><ellipse cx="5" cy="5" rx="1.9" ry="4.3"/><path d="M0.7 5 H9.3 M1.4 2.8 H8.6 M1.4 7.2 H8.6"/></svg>
        <span>www.brightmoor<span class="hl">partners</span>.example</span>
      </li>
    </ul>
  </section>
</body>
</html>
```